Larkwell Bend responsive web design

We need a responsive, bootstrap compatible (but design only - PSD files) website design for a fly fishing shop and guide service.

Design should be very clean. Home Page design + interior page design please.

Possible Home Page Content:
Slide Show
Highlight Three Features: Guided Trips, Fly Shop, Missouri River
About

Thank you and good luck!

Industry/Entity Type

Shop

Requirements
Must have
• This will be used on Bootstrap CMS so needs 12 column bootstrap measurements.

DESIGN ONLY NEEDED (clean PSD files), no programming required.
Need a Home Page layout and secondary page layout

Must show use of the following:
H1 - H5 font uses
link color
Dropdown for navigation bar
Button example
Should not have
• No cutout images, this will be part of CMS and client needs to be able to update most content without knowing photoshop.

```html
<!DOCTYPE html>
<html lang="en">
<head>
<meta charset="utf-8">
<title>Larkwell Bend</title>
<link href="https://fonts.googleapis.com/css2?family=Roboto:wght@400;500;700&display=swap" rel="stylesheet">
<style>
:root{
  --sky:#82d2f0;
  --sand:#ecd9a8;
  --ink:#111;
  --text:#555;
  --body:#333;
  --link:#1768b3;
  --accent:#1598dc;
  --footer:#1d1d1d;
  --white:#fff;
  --rule:#c9c9c9;
}
*{margin:0;padding:0;box-sizing:border-box}
html,body{width:1125px;height:1200px;overflow:hidden;background:var(--white)}
body{position:relative;font-family:'Roboto',Arial,sans-serif;color:var(--body)}
.top-strip{position:absolute;left:0;top:0;width:1125px;height:5px;background:var(--sand)}
.header{position:absolute;left:0;top:5px;width:1125px;height:83px;background:var(--sky)}
.brand{position:absolute;left:190px;top:30px;display:flex;align-items:center;gap:8px;font-size:22px;font-weight:700;color:var(--ink)}
.brand-mark{width:14px;height:14px;background:var(--ink)}
.call{position:absolute;left:780px;top:14px;display:flex;align-items:center}
.call-number{width:90px;height:20px;background:var(--white);border:1px solid #bbb;font-size:8px;line-height:18px;padding-left:14px;color:#222}
.call-btn{width:67px;height:29px;background:var(--accent);color:var(--white);font-size:9px;font-weight:700;display:flex;align-items:center;justify-content:center;gap:4px}
.call-btn svg{width:17px;height:17px}
.nav{position:absolute;left:438px;top:54px;width:687px;height:34px;background:#000;clip-path:polygon(34px 0,100% 0,100% 100%,0 100%)}
.nav a{position:absolute;top:0;line-height:34px;color:var(--white);font-size:9.6px;font-weight:500;text-decoration:none;transform:translateX(-50%);white-space:nowrap}
.hero{position:absolute;left:0;top:88px;width:1125px;height:424px;background:linear-gradient(135deg,#5a5240 0%,#7a6a50 30%,#3b3d3a 60%,#2c2e2c 100%)}
.hero-arrow{position:absolute;top:194px;width:18px;height:30px}
.dots{position:absolute;top:401px;left:530px;display:flex;gap:6px}
.dots span{width:10px;height:10px;border-radius:50%;background:var(--white);border:1px solid #999}
.dots span.on{background:var(--sky)}
.welcome{position:absolute;left:186px;top:524px;width:742px;text-align:center}
.welcome h1{font-size:19px;font-weight:400;color:var(--ink);margin-bottom:8px}
.welcome p{font-size:9.4px;line-height:18px;color:var(--text)}
.feature{position:absolute;top:630px;width:246px;height:170px;border:1px solid #cfe6f0}
.feature-img{height:128px}
.feature-bar{height:42px;background:var(--sky);display:flex;align-items:center;justify-content:space-between;padding:0 14px 0 12px;font-size:13px;color:var(--ink)}
.feature-bar svg{width:20px;height:20px}
.services{position:absolute;left:186px;top:826px;width:508px}
.services h2{font-size:18px;font-weight:400;color:var(--ink);margin-bottom:10px}
.services p{font-size:8.9px;line-height:13.5px;color:var(--text)}
.checklist{position:absolute;top:956px;list-style:none;font-family:Arial,sans-serif;font-size:11px;color:var(--ink)}
.checklist li{position:relative;padding-left:22px;line-height:18px;margin-bottom:3.5px}
.checklist li svg{position:absolute;left:2px;top:3px;width:12px;height:11px}
.news{position:absolute;left:736px;top:840px;width:200px;height:217px;border:1px solid var(--rule);border-radius:8px;padding:12px 10px 0 12px;background:#fbfbfb}
.news-head{display:flex;gap:6px;border-bottom:1px dotted #aaa;padding-bottom:4px}
.news-head svg{width:15px;height:15px;margin-top:3px}
.news-head h3{font-size:15px;font-weight:700;color:var(--link);line-height:16px}
.news-head h4{font-size:9.5px;font-weight:500;color:var(--accent);line-height:11px}
.news-item{padding:16px 0 6px;border-bottom:1px dotted #aaa}
.news-item:last-child{border-bottom:0;padding-top:12px}
.news-date{display:flex;align-items:center;gap:12px;font-size:9px;font-weight:700;color:var(--ink)}
.news-date svg{width:14px;height:13px}
.news-item p{font-size:9px;line-height:13.5px;color:var(--text);margin-top:12px}
.more{display:block;text-align:right;font-size:9px;color:var(--link);text-decoration:none;margin-top:3px}
.footer{position:absolute;left:0;top:1098px;width:1125px;height:102px;background:var(--footer)}
.footer-links{position:absolute;left:187px;top:28px;font-family:Arial,sans-serif;font-size:9px;color:var(--white)}
.footer-links a{color:var(--white);text-decoration:none}
.footer-links b{font-weight:700}
.copyright{position:absolute;left:188px;top:51px;font-family:Arial,sans-serif;font-size:9px;color:var(--white)}
.social{position:absolute;left:840px;top:34px;display:flex;gap:6px}
.social span{width:28px;height:28px;border-radius:50%;background:#ddd;border:2px solid #888}
</style>
</head>
<body>
<div class="top-strip"></div>
<header class="header">
  <div class="brand"><span class="brand-mark"></span>Larkwell Bend</div>
  <div class="call">
    <div class="call-number">555-555-555</div>
    <div class="call-btn"><svg viewBox="0 0 20 20"><circle cx="10" cy="10" r="9" fill="none" stroke="#fff" stroke-width="1.5"/><circle cx="10" cy="8" r="3.3" fill="#fff"/><path d="M4.5 16c1.5-3 3.5-4 5.5-4s4 1 5.5 4" fill="#fff"/></svg>Call Me</div>
  </div>
</header>
<nav class="nav">
  <a href="#" style="left:51px">Home</a>
  <a href="#" style="left:120px">About</a>
  <a href="#" style="left:193px">Fly shop</a>
  <a href="#" style="left:283px">Guide Service</a>
  <a href="#" style="left:382px">Missouri river</a>
  <a href="#" style="left:471px">Contact</a>
</nav>
<section class="hero" role="img" aria-label="Slide photo: two anglers fly fishing from a boat on a river below a hillside">
  <svg class="hero-arrow" style="left:86px" viewBox="0 0 18 30"><path d="M14 2 4 15l10 13" fill="none" stroke="#6fc6ec" stroke-width="5"/></svg>
  <svg class="hero-arrow" style="left:1050px" viewBox="0 0 18 30"><path d="M4 2l10 13L4 28" fill="none" stroke="#6fc6ec" stroke-width="5"/></svg>
  <div class="dots"><span class="on"></span><span></span><span></span></div>
</section>
<section class="welcome">
  <h1>Welcome To Larkwell Bend</h1>
  <p>This theme offers unlimited styling. It's a canvas that lets you build virtually anything: corporate and portfolio sites, blogs, commerce stores or anything else. With vector fonts, latest CSS Beep! is optimized for high resolution displays.This theme offers unlimited styling. It's a canvas that lets you build virtually anything: corporate and portfolio sites, blogs, commerce stores or anything else. With vector fonts, latest CSS Beep! is optimized for high resolution displays.</p>
</section>
<article class="feature" style="left:187px">
  <div class="feature-img" role="img" aria-label="Photo: shop building with a drift boat parked outside" style="background:linear-gradient(180deg,#b9c4cf 0%,#dfe3e6 45%,#8b8475 70%,#56575a 100%)"></div>
  <div class="feature-bar">Guided Trips<svg viewBox="0 0 20 20"><circle cx="10" cy="10" r="10" fill="#000"/><path d="M10 5v10M5 10h10" stroke="#fff" stroke-width="2"/></svg></div>
</article>
<article class="feature" style="left:440px">
  <div class="feature-img" role="img" aria-label="Photo: fly shop interior with gear racks" style="background:linear-gradient(160deg,#e8e2cc 0%,#c79a5a 50%,#7d6a4f 100%)"></div>
  <div class="feature-bar">Fly Shop<svg viewBox="0 0 20 20"><circle cx="10" cy="10" r="10" fill="#000"/><path d="M10 5v10M5 10h10" stroke="#fff" stroke-width="2"/></svg></div>
</article>
<article class="feature" style="left:692px">
  <div class="feature-img" role="img" aria-label="Photo: river at sunset with mountains" style="background:linear-gradient(180deg,#6c86a6 0%,#d9b48b 40%,#b35d2c 60%,#33404d 100%)"></div>
  <div class="feature-bar">Missouri River<svg viewBox="0 0 20 20"><circle cx="10" cy="10" r="10" fill="#000"/><path d="M10 5v10M5 10h10" stroke="#fff" stroke-width="2"/></svg></div>
</article>
<section class="services">
  <h2>Our Services</h2>
  <p>Lorem ipsum dolor sit amet, consectetur adipiscing elit. Nulla convallis egestas rhoncus. Donec facilisis fermentum sem, ac viverra ante luctus vel. Donec vel mauris quam. Lorem ipsum dolor sit amet, consectetur adipiscing elit. Nulla convallis egestas rhoncus. Donec facilisis fermentum sem, ac viverra ante luctus vel. Donec vel mauris quam. Lorem ipsum dolor sit amet, consectetur adipiscing elit. Nulla convallis egestas rhoncus. Donec facilisis fermentum sem, ac viverra ante luctus vel. Donec vel mauris quam. Lorem ipsum dolor sit amet, consectetur adipiscing elit. Nulla convallis egestas rhoncus. Donec facilisis fermentum sem, ac viverra ante luctus vel. Donec vel mauris quam.</p>
</section>
<ul class="checklist" style="left:188px;width:200px">
  <li><svg viewBox="0 0 12 11"><path d="M1 6l3.5 3.5L11 1" fill="none" stroke="#5bb733" stroke-width="2"/></svg>Market Research</li>
  <li><svg viewBox="0 0 12 11"><path d="M1 6l3.5 3.5L11 1" fill="none" stroke="#5bb733" stroke-width="2"/></svg>Channel Distribution &amp; Development</li>
  <li><svg viewBox="0 0 12 11"><path d="M1 6l3.5 3.5L11 1" fill="none" stroke="#5bb733" stroke-width="2"/></svg>Sales/Market Representation</li>
  <li><svg viewBox="0 0 12 11"><path d="M1 6l3.5 3.5L11 1" fill="none" stroke="#5bb733" stroke-width="2"/></svg>Project-Based Market Research</li>
</ul>
<ul class="checklist" style="left:420px;width:220px">
  <li><svg viewBox="0 0 12 11"><path d="M1 6l3.5 3.5L11 1" fill="none" stroke="#5bb733" stroke-width="2"/></svg>Information Forum Events</li>
  <li><svg viewBox="0 0 12 11"><path d="M1 6l3.5 3.5L11 1" fill="none" stroke="#5bb733" stroke-width="2"/></svg>Business Plans</li>
  <li><svg viewBox="0 0 12 11"><path d="M1 6l3.5 3.5L11 1" fill="none" stroke="#5bb733" stroke-width="2"/></svg>Marketing Plans</li>
  <li><svg viewBox="0 0 12 11"><path d="M1 6l3.5 3.5L11 1" fill="none" stroke="#5bb733" stroke-width="2"/></svg>Workshops and Seminars</li>
</ul>
<aside class="news">
  <div class="news-head">
    <svg viewBox="0 0 15 15"><path d="M2 13l1-4 8-8 3 3-8 8z" fill="#f0a030"/></svg>
    <div><h3>Latest news</h3><h4>Be informed</h4></div>
  </div>
  <div class="news-item">
    <div class="news-date"><svg viewBox="0 0 14 13"><rect x="0.5" y="1.5" width="13" height="11" fill="#fff" stroke="#3aa0e0"/><rect x="0.5" y="1.5" width="13" height="3" fill="#3aa0e0"/><path d="M3 7h8M3 9.5h8M5 5v7M9 5v7" stroke="#3aa0e0" stroke-width=".8"/></svg>Mar 10, 2014</div>
    <p>Lorem ipsum dolor sit amet, consectetur adipiscing elit, sed</p>
    <a class="more" href="#">Read More &gt;</a>
  </div>
  <div class="news-item">
    <div class="news-date"><svg viewBox="0 0 14 13"><rect x="0.5" y="1.5" width="13" height="11" fill="#fff" stroke="#3aa0e0"/><rect x="0.5" y="1.5" width="13" height="3" fill="#3aa0e0"/><path d="M3 7h8M3 9.5h8M5 5v7M9 5v7" stroke="#3aa0e0" stroke-width=".8"/></svg>Mar 10, 2014</div>
    <p>Lorem ipsum dolor sit amet, consectetur adipiscing elit, sed</p>
    <a class="more" href="#">Read More &gt;</a>
  </div>
</aside>
<footer class="footer">
  <div class="footer-links"><a href="#">Home</a> &nbsp;|&nbsp; <a href="#">About Us</a> &nbsp;|&nbsp; <a href="#">Services</a> &nbsp;|&nbsp; <a href="#"><b>News/Blog</b></a> &nbsp;|&nbsp; <a href="#"><b>Contact Us</b></a></div>
  <div class="copyright">Copyright Larkwell Bend 2014. &nbsp;All rights reserved.</div>
  <div class="social"><span></span><span></span><span></span></div>
</footer>
</body>
</html>
```